Sign listing benefits of Wash and Fold Service

Sign 48 inches wide and 24 inches height to showcase service listed above.
Benefits include:
Saves Money
Saves Time
Convenient
Stain Treatment

Looking for something colorful (Blue and white are our business colors) the look of a laundromat business.

```html
<!DOCTYPE html>
<html lang="en">
<head>
<meta charset="utf-8">
<title>Wash and Fold Benefits Sign</title>
<link href="https://fonts.googleapis.com/css2?family=Fira+Sans+Condensed:wght@400&family=Fira+Sans:wght@400;600;700&display=swap" rel="stylesheet">
<style>
  :root {
    --blue-deep: #0a90f2;
    --blue-bright: #04b0fd;
    --yellow: #ffd500;
    --navy: #14289a;
    --white: #ffffff;
  }
  * { margin: 0; padding: 0; box-sizing: border-box; }
  html, body { width: 1200px; height: 600px; overflow: hidden; }
  body { background: var(--white); }
  .sign {
    position: relative;
    width: 1200px;
    height: 600px;
    overflow: hidden;
    background: linear-gradient(90deg, var(--blue-deep), var(--blue-bright) 70%);
    font-family: "Fira Sans", sans-serif;
    color: var(--white);
  }
  .backdrop { position: absolute; inset: 0; }
  .headline {
    position: absolute;
    left: 49px;
    top: 44px;
    font-family: "Fira Sans Condensed", sans-serif;
    font-weight: 400;
    font-size: 55px;
    line-height: 50px;
    text-transform: uppercase;
    letter-spacing: 0.2px;
  }
  .headline .accent { color: var(--yellow); }
  .rule {
    position: absolute;
    left: 49px;
    width: 101px;
    height: 4px;
    background: var(--white);
  }
  .rule--top { top: 221px; }
  .rule--bottom { top: 536px; }
  .subhead {
    position: absolute;
    left: 49px;
    top: 249px;
    font-family: "Fira Sans Condensed", sans-serif;
    font-size: 51px;
    line-height: 56px;
    text-transform: uppercase;
  }
  .subhead .accent { color: var(--yellow); }
  .benefits {
    position: absolute;
    left: 49px;
    top: 314px;
    width: 540px;
    display: grid;
    grid-template-columns: 267px 1fr;
    row-gap: 20px;
    list-style: none;
  }
  .benefit {
    display: flex;
    align-items: center;
    gap: 12px;
    height: 38px;
    font-weight: 600;
    font-size: 27px;
  }
  .benefit svg { flex: none; }
  .ready {
    position: absolute;
    left: 432px;
    top: 450px;
    width: 420px;
    height: 61px;
    border-radius: 31px 0 0 31px;
    background: var(--yellow);
    display: flex;
    align-items: center;
    padding-left: 21px;
    gap: 10px;
    color: var(--navy);
    font-weight: 700;
    font-size: 29px;
  }
  .contact {
    position: absolute;
    left: 50px;
    top: 550px;
    display: flex;
    gap: 38px;
    font-size: 27px;
  }
  .contact-item { display: flex; align-items: center; gap: 9px; }
  .contact-item svg { flex: none; }
</style>
</head>
<body>
<main class="sign">
  <svg class="backdrop" width="1200" height="600" viewBox="0 0 1200 600">
    <defs>
      <clipPath id="photo-area">
        <path d="M612 0 C700 60 800 300 806 600 L1200 600 L1200 0 Z"/>
      </clipPath>
      <linearGradient id="ironing-tones" x1="0" y1="0" x2="1" y2="1">
        <stop offset="0" stop-color="#f4f4f2"/>
        <stop offset="0.55" stop-color="#cfe6ee"/>
        <stop offset="1" stop-color="#7aa6d4"/>
      </linearGradient>
      <linearGradient id="laundry-tones" x1="0" y1="0" x2="1" y2="1">
        <stop offset="0" stop-color="#d8c8b4"/>
        <stop offset="0.5" stop-color="#f1ede8"/>
        <stop offset="1" stop-color="#c9b49c"/>
      </linearGradient>
      <radialGradient id="shirts-tones" cx="0.45" cy="0.4" r="0.7">
        <stop offset="0" stop-color="#ef4a3f"/>
        <stop offset="0.6" stop-color="#d8463f"/>
        <stop offset="1" stop-color="#6f8fb8"/>
      </radialGradient>
    </defs>
    <g clip-path="url(#photo-area)">
      <rect x="600" y="0" width="600" height="298" fill="url(#ironing-tones)" role="img" aria-label="Person ironing a shirt on an ironing board"/>
      <rect x="600" y="302" width="600" height="298" fill="url(#laundry-tones)" role="img" aria-label="Smiling woman holding a stack of folded laundry in a laundry room"/>
      <rect x="790" y="298" width="410" height="4" fill="var(--white)"/>
    </g>
    <path d="M612 0 C700 60 800 300 806 600" fill="none" stroke="var(--yellow)" stroke-width="6"/>
    <circle cx="726" cy="300" r="114" fill="var(--yellow)"/>
    <circle cx="726" cy="300" r="106" fill="url(#shirts-tones)" role="img" aria-label="Stack of neatly folded shirts"/>
  </svg>

  <h1 class="headline">
    <span class="accent">The Best</span><br>
    Benefits of Wash<br>
    and Fold Services
  </h1>
  <div class="rule rule--top"></div>

  <h2 class="subhead"><span class="accent">Our</span> Benefits Include:</h2>

  <ul class="benefits">
    <li class="benefit">
      <svg width="38" height="38" viewBox="0 0 38 38" aria-hidden="true"><circle cx="19" cy="19" r="19" fill="var(--navy)"/><path d="M10 19 L17 28 L33 3" fill="none" stroke="var(--yellow)" stroke-width="4.5" stroke-linecap="round" stroke-linejoin="round"/></svg>
      Saves Money
    </li>
    <li class="benefit">
      <svg width="38" height="38" viewBox="0 0 38 38" aria-hidden="true"><circle cx="19" cy="19" r="19" fill="var(--navy)"/><path d="M10 19 L17 28 L33 3" fill="none" stroke="var(--yellow)" stroke-width="4.5" stroke-linecap="round" stroke-linejoin="round"/></svg>
      Saves Time
    </li>
    <li class="benefit">
      <svg width="38" height="38" viewBox="0 0 38 38" aria-hidden="true"><circle cx="19" cy="19" r="19" fill="var(--navy)"/><path d="M10 19 L17 28 L33 3" fill="none" stroke="var(--yellow)" stroke-width="4.5" stroke-linecap="round" stroke-linejoin="round"/></svg>
      Convenient
    </li>
    <li class="benefit">
      <svg width="38" height="38" viewBox="0 0 38 38" aria-hidden="true"><circle cx="19" cy="19" r="19" fill="var(--navy)"/><path d="M10 19 L17 28 L33 3" fill="none" stroke="var(--yellow)" stroke-width="4.5" stroke-linecap="round" stroke-linejoin="round"/></svg>
      Stain Treatment
    </li>
  </ul>

  <div class="ready">
    <svg width="33" height="33" viewBox="0 0 33 33" aria-hidden="true"><circle cx="16.5" cy="16.5" r="16.5" fill="var(--navy)"/><path d="M15 7 V17 L21 23" fill="none" stroke="var(--yellow)" stroke-width="3" stroke-linecap="round"/></svg>
    24/7 Ready to Serve
  </div>

  <div class="rule rule--bottom"></div>

  <div class="contact">
    <span class="contact-item">
      <svg width="18" height="18" viewBox="0 0 18 18" aria-hidden="true"><rect width="18" height="18" fill="var(--navy)"/><path d="M5 4 L7 4 L8 7 L6.5 8 C7.3 9.8 8.4 10.9 10 11.6 L11 10 L14 11 L14 13 C14 13.6 13.5 14 13 14 C8.3 13.7 4.3 9.7 4 5 C4 4.5 4.4 4 5 4 Z" fill="var(--yellow)"/></svg>
      0000 000 000
    </span>
    <span class="contact-item">
      <svg width="18" height="18" viewBox="0 0 18 18" aria-hidden="true"><rect width="18" height="18" fill="var(--navy)"/><g fill="none" stroke="var(--yellow)" stroke-width="1.3"><circle cx="9" cy="9" r="5.5"/><ellipse cx="9" cy="9" rx="2.3" ry="5.5"/><path d="M3.5 9 H14.5"/></g></svg>
      www.website.com
    </span>
  </div>
</main>
</body>
</html>
```